BRW Trifold Brochure

Would like a Trifold Brochure to use for marketing purposes. The company, Bright Ridge Works is a Handyman Service that offers Residential Home Repairs, Commercial Repairs, Drain Cleaning, Carpet Cleaning and Water Extraction.

I am attaching some pdf files to use as potential verbage and a copy of our business card and logo image file.

Would like to portray a professional image that sets us apart from a "mom and pops" type handyman service.

Industry/Entity Type

Marketing

```html
<!DOCTYPE html>
<html lang="en">
<head>
<meta charset="utf-8">
<title>Bright Ridge Works – Trifold Brochure Front</title>
<link rel="stylesheet" href="https://fonts.googleapis.com/css2?family=Arimo:wght@400;700&display=swap">
<style>
  :root {
    --navy: #14254a;
    --ink: #1b2a48;
    --body-grey: #7a7a7a;
    --plum: #8a3f86;
    --plum-light: #b0609f;
    --slate: #55595f;
    --charcoal: #2a2629;
    --panel-grey: #a7b4b8;
    --mint: #cfeae4;
    --white: #ffffff;
    --page-bg: #3a3632;
  }
  * { box-sizing: border-box; margin: 0; padding: 0; }
  html, body { width: 1200px; height: 950px; overflow: hidden; }
  body { background: var(--page-bg); font-family: "Arimo", Arial, sans-serif; position: relative; }

  .brochure { position: absolute; left: 50px; top: 72px; width: 1100px; height: 846px; background: var(--white); overflow: hidden; }

  /* Left panel */
  .info-panel { position: absolute; left: 0; top: 0; width: 368px; height: 846px; background: var(--white); }
  .panel-title { position: absolute; left: 12px; top: 13px; width: 343px; height: 48px; }
  .panel-title svg { position: absolute; inset: 0; }
  .panel-title h2 { position: absolute; left: 14px; top: 13px; color: var(--white); font-size: 19px; font-weight: 700; }
  .info-copy { position: absolute; left: 19px; top: 80px; width: 336px; }
  .info-copy h3 { color: var(--ink); font-size: 12.5px; font-weight: 700; line-height: 24px; }
  .info-copy h4 { color: var(--ink); font-size: 12.5px; font-weight: 400; line-height: 24px; }
  .info-copy p { color: var(--body-grey); font-size: 12px; line-height: 23.3px; text-align: justify; margin-bottom: 8px; }
  .call-band { position: absolute; left: 0; top: 625px; width: 368px; height: 221px; }
  .call-band svg { position: absolute; inset: 0; }
  .call-text { position: absolute; left: 0; top: 50px; width: 368px; text-align: center; color: var(--white); }
  .call-text .line { font-size: 20px; line-height: 29px; }
  .call-text .line.gap { margin-top: 8px; }
  .call-text .big { font-size: 25px; line-height: 35px; }

  /* Cover panel */
  .cover { position: absolute; left: 368px; top: 0; width: 732px; height: 846px; background: linear-gradient(160deg, var(--panel-grey) 40%, var(--mint) 100%); }
  .cover-photo { position: absolute; left: 0; top: 0; width: 732px; height: 450px; background: linear-gradient(180deg, #c9cfcf 0%, #b9b3a7 45%, #caa98c 100%); clip-path: path("M0 0 H732 V360 Q380 352 0 448 Z"); }
  .cover-curve { position: absolute; left: 0; top: 0; }
  .brand-name { position: absolute; color: var(--navy); font-weight: 700; text-align: center; font-size: 31px; line-height: 34px; }
  .brand-top { left: 422px; top: 455px; width: 270px; }
  .brand-bottom { left: 62px; top: 655px; width: 250px; font-size: 29px; }
  .service-tag { position: absolute; left: 478px; top: 548px; width: 206px; height: 62px; }
  .service-tag .box { position: absolute; left: 10px; top: 0; width: 196px; height: 60px; border-radius: 4px; background: linear-gradient(180deg, #ffffff, #e3e6e8); box-shadow: 0 2px 4px rgba(0,0,0,.25); }
  .service-tag .stub { position: absolute; left: 0; top: 8px; width: 20px; height: 50px; background: #8dc63f; border-radius: 3px; }
  .service-tag svg { position: absolute; left: 4px; top: 2px; }
  .service-tag p { position: absolute; left: 45px; top: 12px; color: var(--ink); font-size: 16px; font-weight: 700; line-height: 19px; }
  .service-list { position: absolute; left: 432px; top: 636px; list-style: none; }
  .service-list li { color: #4f5a66; font-size: 16px; line-height: 31px; padding-left: 18px; position: relative; }
  .service-list li::before { content: ""; position: absolute; left: 0; top: 13px; width: 6px; height: 6px; border-radius: 50%; background: #3a3f46; }
  .contact-placeholder { position: absolute; left: 40px; top: 730px; width: 300px; text-align: center; color: #4d5358; font-size: 22px; line-height: 28px; }
  .footer-strip { position: absolute; left: 0; top: 806px; width: 732px; height: 40px; background: var(--charcoal); border-top: 2px solid #d8dadb; color: #e6e6e6; font-size: 20px; }
  .footer-strip .site { position: absolute; left: 52px; top: 7px; letter-spacing: 4px; }
  .footer-strip .phone { position: absolute; right: 22px; top: 7px; letter-spacing: 1px; }
</style>
</head>
<body>
<main class="brochure">
  <section class="info-panel">
    <div class="panel-title">
      <svg width="343" height="48" viewBox="0 0 343 48" aria-hidden="true">
        <defs>
          <linearGradient id="plumGrad" x1="0" x2="1" y1="0" y2="0">
            <stop offset="0" stop-color="#7e3a80"/>
            <stop offset="1" stop-color="#b36aa8"/>
          </linearGradient>
        </defs>
        <polygon points="270,0 343,0 296,48 223,48" fill="#5b5f66"/>
        <polygon points="0,0 293,0 248,48 0,48" fill="url(#plumGrad)"/>
      </svg>
      <h2>Harlow Carpet Cleaning</h2>
    </div>
    <div class="info-copy">
      <h3>It's Your Carpet, How Clean is it?</h3>
      <h4>Carpet Cleaning</h4>
      <p>Carpet is one of the most used items in our household and yet is often the most ignored. Dirt, Sand, Food, Dander, Dead Skin, Hair, Grease and oil all build up over time. Sure you vacuum but is it doing enough? The answer is no! Let us take care of your carpet cleaning needs with our experienced technicans and the right equipment fo. the job.</p>
      <h3>Mile &amp; Grout Cleaning. The Results</h3>
      <h4>Speak for Themselves!!!</h4>
      <p>It only takes once before you are a believer! Tile and grout build up layers of dirt and grime over time. Mopping and scrubbing go a long way but from time to time they need a deep clean. That is where Bright Ridge Works comes in, Regardless of where the tile is we can make a difference for you!</p>
      <h3>Emergency Water Extraction!!!</h3>
      <p>Water does serious damage. When there is an emergency, timing is of the essence. When lhat pipe breaks or a back up occurs call us and we'll be lhere. Our knowledgable staff and is equipped with the resources to give you the best chance of salvaging your carpet after a majorwater issue. Call Today to see how we can help!!!</p>
    </div>
    <div class="call-band">
      <svg width="368" height="221" viewBox="0 0 368 221" aria-hidden="true">
        <path d="M0 20 Q190 -4 368 8 V221 H0 Z" fill="#1b2f5c"/>
        <path d="M0 42 Q190 22 368 32 V221 H0 Z" fill="#2a2629"/>
      </svg>
      <div class="call-text">
        <div class="line">Call Today!!!</div>
        <div class="line">(555) 014 - 2290</div>
        <div class="line gap">We are Available</div>
        <div class="big">24/7 for Emergency</div>
        <div class="big">Water Extraction!!!</div>
      </div>
    </div>
  </section>

  <section class="cover">
    <div class="cover-photo" role="img" aria-label="Photo of two workers in hard hats laying floor tiles beside large windows"></div>
    <svg class="cover-curve" width="732" height="470" viewBox="0 0 732 470" aria-hidden="true">
      <path d="M0 448 Q380 352 732 360 V376 Q380 372 0 470 Z" fill="#14254a"/>
    </svg>
    <div class="brand-name brand-top">Bright Ridge Works</div>
    <div class="service-tag">
      <div class="stub"></div>
      <div class="box"></div>
      <svg width="36" height="60" viewBox="0 0 36 60" aria-hidden="true">
        <path d="M6 4 Q22 4 22 22 V40 H30 L16 58 L2 40 H10 V22 Q10 14 6 14 Z" fill="#3fa9d6"/>
      </svg>
      <p>Handyman Service<br>that offers</p>
    </div>
    <ul class="service-list">
      <li>Residential Home Repairs</li>
      <li>Commercial Repairs</li>
      <li>Drain Cleaning</li>
      <li>Carpet Cleaning</li>
      <li>Water Extraction</li>
    </ul>
    <div class="brand-name brand-bottom">Bright Ridge Works</div>
    <p class="contact-placeholder">Put yourAddress and contact information here</p>
    <div class="footer-strip">
      <span class="site">www.website.com</span>
      <span class="phone">Call Today!!! (555) 014 - 2290</span>
    </div>
  </section>
</main>
</body>
</html>
```